Harborline Motors LLC

Car Dealer Customer Service
Address: 2741 Linden Avenue, Shelbyville, TN 37162
web: www.harborlinemotorstn.net
email: harborlinemotorstn@mailbox-example.net
Phone: (931) 555-0148
Phone: (629) 555-0173

```html
<!DOCTYPE html>
<html lang="en">
<head>
<meta charset="utf-8">
<title>Harborline Motors – Business Card</title>
<link href="https://fonts.googleapis.com/css2?family=Montserrat:wght@800&family=Oswald:wght@300;600&family=Poppins:wght@300;400&display=swap" rel="stylesheet">
<style>
  :root {
    --page: #ffffff;
    --front-bg: #bdcdd6;
    --back-bg: #d3d3d3;
    --brand-blue: #1e77a8;
    --ink-dark: #27343e;
    --ink-soft: #3f464c;
  }
  * { margin: 0; padding: 0; box-sizing: border-box; }
  html, body {
    width: 1077px; height: 1200px; overflow: hidden;
    background: var(--page);
  }
  .canvas { position: relative; width: 1077px; height: 1200px; }

  .card {
    position: absolute; left: 262px; width: 565px; height: 339px; overflow: hidden;
  }
  .card--front { top: 224px; background: var(--front-bg); }
  .card--back  { top: 650px; background: var(--back-bg); }

  .brand {
    position: absolute; display: flex; flex-direction: column; align-items: center;
  }
  .brand__dot {
    border-radius: 50%; background: var(--brand-blue);
  }
  .brand__name {
    font-family: "Montserrat", sans-serif; font-weight: 800;
    color: var(--brand-blue); white-space: nowrap; letter-spacing: 0.2px;
  }
  .card--front .brand { left: 0; right: 0; top: 108px; }
  .card--front .brand__dot { width: 44px; height: 44px; margin-bottom: 22px; }
  .card--front .brand__name { font-size: 22px; }

  .card--back .brand { left: 0; width: 278px; top: 130px; }
  .card--back .brand__dot { width: 38px; height: 38px; margin-bottom: 20px; }
  .card--back .brand__name { font-size: 17px; }

  .divider {
    position: absolute; left: 277px; top: 54px; width: 1.5px; height: 224px;
    background: var(--brand-blue);
  }

  .person { position: absolute; left: 317px; top: 50px; }
  .person__name {
    font-family: "Oswald", sans-serif; font-size: 26px; line-height: 1;
    letter-spacing: 3px; color: var(--ink-dark); text-transform: uppercase;
  }
  .person__first { font-weight: 600; }
  .person__last { font-weight: 300; color: var(--ink-soft); }
  .person__role {
    font-family: "Poppins", sans-serif; font-weight: 400; font-size: 12px;
    letter-spacing: 1.6px; color: var(--ink-soft); margin-top: 1px;
  }

  .contacts {
    position: absolute; left: 317px; top: 156px; right: 20px; list-style: none;
    font-family: "Poppins", sans-serif; font-weight: 300; font-size: 10.5px;
    line-height: 13px; letter-spacing: 0.6px; color: var(--ink-soft);
  }
  .contact { display: flex; align-items: center; margin-bottom: 11px; white-space: nowrap; }
  .contact__icon { width: 20px; height: 20px; flex: none; margin-right: 12px; }
  .contact__icon svg { width: 20px; height: 20px; display: block; }
  .contact--email { letter-spacing: 0; font-size: 9px; }
</style>
</head>
<body>
<div class="canvas">

  <section class="card card--front">
    <div class="brand">
      <span class="brand__dot"></span>
      <span class="brand__name">HARBORLINE MOTORS</span>
    </div>
  </section>

  <section class="card card--back">
    <div class="brand">
      <span class="brand__dot"></span>
      <span class="brand__name">HARBORLINE MOTORS</span>
    </div>

    <div class="divider"></div>

    <div class="person">
      <h1 class="person__name"><span class="person__first">Marcus</span> <span class="person__last">Hale</span></h1>
      <p class="person__role">DIRECTOR</p>
    </div>

    <ul class="contacts">
      <li class="contact">
        <span class="contact__icon">
          <svg viewBox="0 0 20 20" fill="none" stroke="#1e77a8" stroke-width="1.2">
            <path d="M3.5 17.5 L4.6 14 A8 8 0 1 1 7.2 16.6 Z"/>
            <path d="M7.2 6.2 l1.4-.4 1 2.1-.9.8 a5 5 0 0 0 2.5 2.5 l.8-.9 2.1 1-.4 1.4 c-3 .8-7.2-3.4-6.5-6.5z"/>
          </svg>
        </span>
        <span>(931) 555-0148<br>(629) 555-0173</span>
      </li>
      <li class="contact">
        <span class="contact__icon">
          <svg viewBox="0 0 20 20" fill="none" stroke="#1e77a8" stroke-width="1.2">
            <path d="M2 9 L9 2.5 L13 6.2 M4 7.5 V16.5 H9"/>
            <path d="M13 18 c-3-3.2-4.2-5-4.2-6.6 a4.2 4.2 0 0 1 8.4 0 c0 1.6-1.2 3.4-4.2 6.6z"/>
            <circle cx="13" cy="11.3" r="1.4"/>
          </svg>
        </span>
        <span>2741 Linden Avenue<br>Shelbyville, TN 37162</span>
      </li>
      <li class="contact">
        <span class="contact__icon">
          <svg viewBox="0 0 20 20" fill="none" stroke="#1e77a8" stroke-width="1.2">
            <circle cx="10" cy="10" r="8.5"/>
            <circle cx="10" cy="10" r="5.5"/>
            <ellipse cx="10" cy="10" rx="2.3" ry="5.5"/>
            <path d="M4.5 10 H15.5 M5.3 7.5 H14.7 M5.3 12.5 H14.7"/>
          </svg>
        </span>
        <span>www.harborlinemotorstn.net</span>
      </li>
      <li class="contact contact--email">
        <span class="contact__icon">
          <svg viewBox="0 0 20 20" fill="none" stroke="#1e77a8" stroke-width="1.2">
            <circle cx="10" cy="10" r="8.5"/>
            <circle cx="10" cy="10" r="2.4"/>
            <path d="M12.4 8 V11.2 a1.6 1.6 0 0 0 3.2 0 V10 a5.6 5.6 0 1 0 -2.2 4.5"/>
          </svg>
        </span>
        <span>harborlinemotorstn@mailbox-example.net</span>
      </li>
    </ul>
  </section>

</div>
</body>
</html>
```